Labels/logo for luxury bath products

I am developing a range of luxury bath foams - aimed at the top end of the luxury market. My company name is VEM (very basic website can be seen at www.vemarton.example).

I am looking for a label design for the front of the bottle, which should incorporate the VEM logo as per the website (file attached), but embedded within a more intricate label design. I provide a link to a picture of the bottle below.

The bath foam will come in four fragrances: Vetiver, Sandalwood, Jasmine and Neroli. The label should include the fragrance name. So the label must include the brand name 'VEM' and the name of the fragrance - e.g. Sandalwood Bath Foam, Neroli Bath Foam, etc.

The products are aimed at both the male and female market and so shouldn't be too feminine.

A brand to take inspiration from is Lune Bravière: http://www.lunebraviere.example/ - I like the labels that they use on their products, which is a gold embossed crest, which they use as the label for their products. I am not referring to their font, but to their label design - I like the embossed label, and am quite keen on metallics.

Conversely, I would like to add a contemporary edge to this design - I like the striping and contemporary fonts on this design: http://www.hadley-frost.example/images/fac83.jpg

My brand also harnesses the powers of natural flower ingredients, and so I am inspired by the products of Quenby - quenby.example. This labelling is more clinical and scientific.

Ideally I would like a label which combines these elements - i.e. a luxury label with a contemporary feel, that incorporate the scientific nature of the product.

The design needs to communicate high end luxury. The bottle is however apothecary style, and a nod to science and botany would be good. I would however like a bold approach to this design - it is a modern brand.

The bottle being used for the product can be seen at: http://www.tavel-vitro.example/en/product-groups/8-Apothecary-bottles - these are extremely expensive bottles and the label needs to reflect this quality. These bottles are traditional in design, but incorporate high end glassware technology to preserve the integrity of the natural ingredients. Therefore the product is a mix of old and new, and the label could also reflect this. The colour of the glass is very deep purple.

The front label does not need information such as weight/volume - it purely needs a label which will recognise it as the VEM brand, with the product name. I am looking for a high quality label, which is unique. I am happy to print embossed labels and to use foils on my labels.

Please do not be boring! I appreciate I have given a variety of influences, so summarise the requirements are a mix of:

a bold design
contemporary
luxury

The label must include NO slogans.

I am looking to build a relationship with a graphic designer for packaging and website design requirements so this will be the first of many projects.

Target Market(s)

Luxury end of market - clientele will like luxury and will pay for the highest quality ingredients in the product, but will also appreciate the botanical nature of the product.

Industry/Entity Type

Graphic Designer

Requirements
Must have
• Must include the company name, VEM, although this doesn't need to be particularly prominent. And the product name, e.g. Sandalwood.
Nice to have
• It should combine luxury, but with recognition of the science behind the product.
Should not have
• No slogans, minimal wording on the front label. No other wording other than company name and product name. No primary colours.

```html
<!DOCTYPE html>
<html lang="en">
<head>
<meta charset="utf-8">
<title>VEM Jasmine Bath Foam – Front Label</title>
<link rel="stylesheet" href="https://fonts.googleapis.com/css2?family=PT+Sans:wght@700&family=PT+Sans+Narrow:wght@700&family=PT+Serif:wght@700&display=swap">
<style>
  :root {
    --canvas-bg: #ffffff;
    --label-teal: #3a9eaa;
    --foam-light: #4aa9b3;
    --foam-dark: #3596a2;
    --ink: #231f20;
    --volume-ink: #86655d;
    --gold-light: #e9d9b6;
    --gold-mid: #a88a5c;
    --bronze: #7a5330;
    --bronze-dark: #6a4a2c;
  }
  html, body {
    margin: 0;
    padding: 0;
    width: 1200px;
    height: 1000px;
    overflow: hidden;
    background: var(--canvas-bg);
  }
  .canvas {
    position: relative;
    width: 1200px;
    height: 1000px;
  }
  .front-label {
    position: absolute;
    left: 277px;
    top: 177px;
    width: 646px;
    height: 646px;
    display: block;
  }
  .brand-name {
    font-family: "PT Sans", "Helvetica Neue", Arial, sans-serif;
    font-weight: 700;
    fill: var(--ink);
  }
  .product-type {
    font-family: "PT Sans", "Helvetica Neue", Arial, sans-serif;
    font-weight: 700;
    font-size: 29px;
    fill: var(--ink);
  }
  .fragrance-name {
    font-family: "PT Sans Narrow", "Arial Narrow", sans-serif;
    font-weight: 700;
    font-size: 56px;
    fill: var(--ink);
  }
  .net-volume {
    font-family: "PT Serif", Georgia, serif;
    font-weight: 700;
    font-size: 18px;
    fill: var(--volume-ink);
  }
</style>
</head>
<body>
<main class="canvas">
  <svg class="front-label" viewBox="0 0 646 646" role="group" aria-label="VEM Jasmine bath foam label">
    <defs>
      <linearGradient id="metallicFrame" x1="0" y1="0" x2="1" y2="1">
        <stop offset="0" stop-color="var(--gold-mid)"/>
        <stop offset="0.12" stop-color="var(--gold-light)"/>
        <stop offset="0.35" stop-color="var(--gold-mid)"/>
        <stop offset="0.55" stop-color="var(--bronze)"/>
        <stop offset="0.75" stop-color="var(--bronze-dark)"/>
        <stop offset="0.9" stop-color="var(--gold-light)"/>
        <stop offset="1" stop-color="var(--gold-mid)"/>
      </linearGradient>
      <linearGradient id="foamTone" x1="0" y1="0" x2="1" y2="1">
        <stop offset="0" stop-color="var(--foam-light)"/>
        <stop offset="1" stop-color="var(--foam-dark)"/>
      </linearGradient>
    </defs>

    <rect class="label-frame" x="0" y="0" width="646" height="646" fill="url(#metallicFrame)"/>
    <rect class="label-field" x="31" y="31" width="585" height="585" fill="var(--label-teal)"/>

    <text class="brand-name" transform="translate(259 576) rotate(-90)" font-size="280" textLength="508" lengthAdjust="spacingAndGlyphs">VEM</text>

    <rect class="foam-illustration" x="272" y="50" width="318" height="370" rx="24" fill="url(#foamTone)" role="img" aria-label="Copper line illustration of a cloud of foam bubbles"/>

    <text class="product-type" x="410" y="273" text-anchor="middle">bath foam</text>
    <text class="fragrance-name" x="429" y="508" text-anchor="middle">JASMINE</text>
    <text class="net-volume" x="429" y="571" text-anchor="middle">NET VOL 253 PL OZ</text>
    <text class="net-volume" x="429" y="601" text-anchor="middle">NET VOL 750ml e</text>
  </svg>
</main>
</body>
</html>
```